Webdesign for Property Renting Business

We need a professional and slim design for a hight quality property renting website which is not overcrowded with too much information and has a clear and easily structure to read. The visitor should get an instant impression what he can do at a glance.

The goal of this contest is to get a design for building a prototype of the website and to attract our client and owner of the site by a good looking prototype and not just a wireframe. Therefore we don't need an HTML-coded design at this early project-stage. We only expect getting a simple bitmap or vector-graphic design.

Actually we don't have a logo. Use a placeholder or feel free to design a simple one by yourself.

Last but not least if you have a good idea just include it in to your design.
Updates

Our goal is to get a design for building a prototype of the website and to attract our client by a good looking prototype and not just a wireframe.

Target Market(s)

People who want to spend money to rent a good quality property. Not only the riches. These could be business people and also demanding families as well.

Industry/Entity Type

Building

Colors
85cae6

Requirements
Must have
• We need two sites, a start site and a property-details site. Each site has to include the following points:

1.) start site
- search mask (location, date to choose, quanity of guests)
- show some properties (highlights, special offers etc.)
- show login/register link

2.) property site
- Location in Plorvex Map
- Photos, Description, Amenities, Calendar (available,not available), Contact, Reviews

These are some sites which I like from a design prospective
- http://www.stayquill.example
- http://www.lodgeniv.example/
- http://www.roomtavel.example/
- http://www.brunolap.example

These are some sites which I dislike:
1.) http://www.marvelin-homes.example/guides/france/rent/
2.) http://www.quenlodrest.example/property-rentals.htm

We don't need an HTML-coded design at this early project-stage. We only expect getting a simple bitmap or vector-graphic design. Maybe with the PSD-file (or wathever program you use) that we can pick-out some elements for building the prototype.

```html
<!DOCTYPE html>
<html lang="en">
<head>
<meta charset="utf-8">
<title>Nestwell – Property Rentals</title>
<link href="https://fonts.googleapis.com/css2?family=Lato:ital,wght@0,300;0,400;0,700;0,900;1,300;1,400&display=swap" rel="stylesheet">
<style>
  :root{
    --nav-blue:#85cae6;
    --band-blue:#6a95b0;
    --accent:#29a9e8;
    --ink:#1f2a30;
    --nav-ink:#34424a;
    --white:#ffffff;
    --tag-green:#2d7d22;
    --diamond:#7cc4d6;
    --edge:#5b88a3;
  }
  *{box-sizing:border-box;margin:0;padding:0}
  html,body{width:1200px;height:935px;overflow:hidden;background:var(--band-blue)}
  body{font-family:'Lato',sans-serif;position:relative}
  .page{position:relative;width:1200px;height:935px;overflow:hidden;background:var(--band-blue)}

  .topbar{position:absolute;left:0;top:0;width:1200px;height:40px;background:var(--nav-blue);z-index:3}
  .topbar a{position:absolute;top:11px;font-size:14px;color:var(--nav-ink);text-decoration:none}
  .topbar a.current{color:var(--white)}
  .social{position:absolute;top:0;height:40px;width:47px}
  .social::after{content:"";position:absolute;left:17px;top:13px;width:13px;height:13px;border-radius:50%;background:var(--white);opacity:.9}
  .divider{position:absolute;top:0;width:1px;height:40px;background:rgba(255,255,255,.45)}

  .hero{position:absolute;left:0;top:40px;width:1200px;height:552px;
    background:
      radial-gradient(ellipse 18% 35% at 50% 62%, rgba(214,172,78,.85), rgba(214,172,78,0) 100%),
      linear-gradient(180deg, rgba(0,0,0,0) 55%, rgba(20,16,12,.35) 100%),
      linear-gradient(90deg,#3f332c 0%,#5a4a40 18%,#7d756d 36%,#8f8c86 50%,#a09d97 64%,#8a837c 82%,#6a5f58 100%);}

  .brand{position:absolute;left:0;width:1200px;top:82px;text-align:center;z-index:2;
    font-size:34px;font-weight:900;color:var(--white);letter-spacing:1px}
  .brand .mark{display:inline-block;width:16px;height:16px;background:var(--nav-blue);margin-right:10px;vertical-align:4px}

  .login{position:absolute;left:476px;top:186px;width:254px;height:49px;border:3px solid var(--white);
    color:var(--white);font-size:20px;display:flex;align-items:center;justify-content:center;gap:12px;z-index:2}

  .search-frame{position:absolute;left:238px;top:273px;width:729px;height:60px;border:3px solid rgba(235,235,235,.85);border-radius:4px;z-index:2}
  .field{position:absolute;top:283px;height:40px;background:var(--white);font-size:20px;color:#2b2b2b;display:flex;align-items:center;padding-left:10px;z-index:2}
  .field.location{left:247px;width:273px;border:2px solid var(--accent)}
  .field.date{left:524px;width:203px}
  .field.guest{left:733px;width:139px;padding-left:24px}
  .field svg{position:absolute;right:10px}
  .search-btn{position:absolute;left:877px;top:283px;width:80px;height:40px;background:var(--accent);color:var(--white);font-size:20px;display:flex;align-items:center;justify-content:center;z-index:2}

  .card{position:absolute;top:449px;width:326px;height:282px;z-index:2}
  .card svg.shape{position:absolute;left:0;top:0}
  .card .tools{position:absolute;top:110px;left:0;width:326px;display:flex;justify-content:center;gap:12px}
  .diamond{width:34px;height:34px;transform:rotate(45deg);background:var(--diamond);opacity:.9;display:flex;align-items:center;justify-content:center}
  .diamond svg{transform:rotate(-45deg)}
  .card h3{position:absolute;top:152px;width:100%;text-align:center;font-size:19px;font-weight:400;letter-spacing:1.2px;color:var(--ink)}
  .card .tagline{position:absolute;top:175px;width:100%;text-align:center;font-size:13px;font-style:italic;color:var(--tag-green)}
  .card .badge{position:absolute;top:198px;left:134px;width:58px;height:58px;border-radius:50%;background:var(--accent);color:var(--white);font-size:12px;font-weight:900;display:flex;align-items:center;justify-content:center}

  .nav-arrow{position:absolute;top:571px;z-index:2}

  .promo-title{position:absolute;left:43px;top:818px;font-size:33px;font-style:italic;font-weight:300;color:var(--white);letter-spacing:1px}
  .promo-sub{position:absolute;left:240px;top:859px;font-size:14px;font-style:italic;color:var(--white)}
  .more{position:absolute;left:902px;top:826px;width:176px;height:42px;background:var(--white);display:flex;align-items:center;padding-left:24px;font-size:22px;font-style:italic;color:var(--ink);letter-spacing:1px}
  .more svg{position:absolute;right:18px;top:5px}
</style>
</head>
<body>
<div class="page">
  <nav class="topbar">
    <a class="current" style="left:54px">Home</a>
    <a style="left:123px">Listing</a>
    <a style="left:197px">News</a>
    <a style="left:263px">IDX</a>
    <a style="left:320px">Gallery</a>
    <a style="left:400px">Blog</a>
    <a style="left:467px">Types</a>
    <a style="left:536px">Contact us</a>
    <span class="social" style="left:906px"></span>
    <span class="divider" style="left:949px"></span>
    <span class="social" style="left:952px"></span>
    <span class="divider" style="left:999px"></span>
    <span class="social" style="left:1000px"></span>
    <span class="divider" style="left:1046px"></span>
    <span class="social" style="left:1047px"></span>
    <span class="divider" style="left:1094px"></span>
    <span class="social" style="left:1094px"></span>
  </nav>

  <div class="hero" role="img" aria-label="City street between tall apartment buildings with warm evening light"></div>

  <div class="brand"><span class="mark"></span>Nestwell</div>

  <div class="login">Log in / Register
    <svg width="18" height="12" viewBox="0 0 18 12"><path d="M2 2l7 7 7-7" fill="none" stroke="#fff" stroke-width="3"/></svg>
  </div>

  <div class="search-frame"></div>
  <div class="field location">Search location</div>
  <div class="field date">Date
    <svg width="22" height="22" viewBox="0 0 22 22"><rect x="1" y="3" width="20" height="18" fill="none" stroke="#9aa" stroke-width="1.5"/><line x1="1" y1="8" x2="21" y2="8" stroke="#9aa" stroke-width="1.5"/><g fill="#9aa"><rect x="4" y="11" width="3" height="3"/><rect x="9.5" y="11" width="3" height="3"/><rect x="15" y="11" width="3" height="3"/><rect x="4" y="16" width="3" height="3"/><rect x="9.5" y="16" width="3" height="3"/><rect x="15" y="16" width="3" height="3"/></g></svg>
  </div>
  <div class="field guest">Guest
    <svg width="10" height="8" viewBox="0 0 10 8"><path d="M0 0h10L5 8z" fill="#444"/></svg>
  </div>
  <div class="search-btn">Search</div>

  <svg class="nav-arrow" style="left:44px" width="26" height="44" viewBox="0 0 26 44"><path d="M23 2L3 22l20 20" fill="none" stroke="#fff" stroke-width="3"/></svg>
  <svg class="nav-arrow" style="left:1141px" width="26" height="44" viewBox="0 0 26 44"><path d="M3 2l20 20L3 42" fill="none" stroke="#fff" stroke-width="3"/></svg>

  <!-- property cards -->
  <article class="card" style="left:99px">
    <svg class="shape" width="326" height="282" viewBox="0 0 326 282">
      <defs><linearGradient id="houseA" x1="0" y1="0" x2="0" y2="1"><stop offset="0" stop-color="#8fb9d6"/><stop offset=".45" stop-color="#b8a48c"/><stop offset=".75" stop-color="#7d8a4e"/><stop offset="1" stop-color="#5f7d3a"/></linearGradient></defs>
      <polygon points="84,1 242,1 325,141 242,281 84,281 1,141" fill="none" stroke="#fff" stroke-width="2"/>
      <polygon points="14,144 312,144 238,276 88,276" fill="var(--edge)"/>
      <polygon points="10,141 316,141 238,272 92,272" fill="#fff"/>
      <polygon points="88,7 238,7 317,141 9,141" fill="url(#houseA)" role="img" aria-label="Photo of a colonial style house with white columns"/>
    </svg>
    <div class="tools">
      <div class="diamond"><svg width="18" height="18" viewBox="0 0 18 18"><g fill="none" stroke="#4d7f8e" stroke-width="2.4"><rect x="1" y="7" width="9" height="5" rx="2.5" transform="rotate(-45 5.5 9.5)"/><rect x="8" y="6" width="9" height="5" rx="2.5" transform="rotate(-45 12.5 8.5)"/></g></svg></div>
      <div class="diamond"><svg width="18" height="18" viewBox="0 0 18 18"><g stroke="#4d7f8e" stroke-width="2.4" fill="#4d7f8e"><line x1="3" y1="3" x2="15" y2="15"/><line x1="15" y1="3" x2="3" y2="15"/><path d="M1 1h6L1 7z M17 1h-6l6 6z M1 17h6l-6-6z M17 17h-6l6-6z" stroke="none"/></g></svg></div>
    </div>
    <h3>LOREM IPSUM</h3>
    <p class="tagline">Lorem Ipsum Dolor sit</p>
    <div class="badge">10% OFF</div>
  </article>

  <article class="card" style="left:444px">
    <svg class="shape" width="326" height="282" viewBox="0 0 326 282">
      <defs><linearGradient id="houseB" x1="0" y1="0" x2="0" y2="1"><stop offset="0" stop-color="#6f7b83"/><stop offset=".4" stop-color="#c9c3b8"/><stop offset=".7" stop-color="#7d9a48"/><stop offset="1" stop-color="#6e9140"/></linearGradient></defs>
      <polygon points="84,1 242,1 325,141 242,281 84,281 1,141" fill="none" stroke="#fff" stroke-width="2"/>
      <polygon points="14,144 312,144 238,276 88,276" fill="var(--edge)"/>
      <polygon points="10,141 316,141 238,272 92,272" fill="#fff"/>
      <polygon points="88,7 238,7 317,141 9,141" fill="url(#houseB)" role="img" aria-label="Photo of a single storey house with a porch and lawn"/>
    </svg>
    <div class="tools">
      <div class="diamond"><svg width="18" height="18" viewBox="0 0 18 18"><g fill="none" stroke="#4d7f8e" stroke-width="2.4"><rect x="1" y="7" width="9" height="5" rx="2.5" transform="rotate(-45 5.5 9.5)"/><rect x="8" y="6" width="9" height="5" rx="2.5" transform="rotate(-45 12.5 8.5)"/></g></svg></div>
      <div class="diamond"><svg width="18" height="18" viewBox="0 0 18 18"><g stroke="#4d7f8e" stroke-width="2.4" fill="#4d7f8e"><line x1="3" y1="3" x2="15" y2="15"/><line x1="15" y1="3" x2="3" y2="15"/><path d="M1 1h6L1 7z M17 1h-6l6 6z M1 17h6l-6-6z M17 17h-6l6-6z" stroke="none"/></g></svg></div>
    </div>
    <h3>LOREM IPSUM</h3>
    <p class="tagline">Lorem Ipsum Dolor sit</p>
    <div class="badge">15% OFF</div>
  </article>

  <article class="card" style="left:786px">
    <svg class="shape" width="326" height="282" viewBox="0 0 326 282">
      <defs><linearGradient id="houseC" x1="0" y1="0" x2="0" y2="1"><stop offset="0" stop-color="#4f8a3a"/><stop offset=".35" stop-color="#e4e6e8"/><stop offset=".6" stop-color="#c88a4a"/><stop offset=".8" stop-color="#5c9a34"/><stop offset="1" stop-color="#4f8a2c"/></linearGradient></defs>
      <polygon points="84,1 242,1 325,141 242,281 84,281 1,141" fill="none" stroke="#fff" stroke-width="2"/>
      <polygon points="14,144 312,144 238,276 88,276" fill="var(--edge)"/>
      <polygon points="10,141 316,141 238,272 92,272" fill="#fff"/>
      <polygon points="88,7 238,7 317,141 9,141" fill="url(#houseC)" role="img" aria-label="Photo of a modern white villa with lit living room and garden"/>
    </svg>
    <div class="tools">
      <div class="diamond"><svg width="18" height="18" viewBox="0 0 18 18"><g fill="none" stroke="#4d7f8e" stroke-width="2.4"><rect x="1" y="7" width="9" height="5" rx="2.5" transform="rotate(-45 5.5 9.5)"/><rect x="8" y="6" width="9" height="5" rx="2.5" transform="rotate(-45 12.5 8.5)"/></g></svg></div>
      <div class="diamond"><svg width="18" height="18" viewBox="0 0 18 18"><g stroke="#4d7f8e" stroke-width="2.4" fill="#4d7f8e"><line x1="3" y1="3" x2="15" y2="15"/><line x1="15" y1="3" x2="3" y2="15"/><path d="M1 1h6L1 7z M17 1h-6l6 6z M1 17h6l-6-6z M17 17h-6l6-6z" stroke="none"/></g></svg></div>
    </div>
    <h3>LOREM IPSUM</h3>
    <p class="tagline">Lorem Ipsum Dolor sit</p>
    <div class="badge">10% OFF</div>
  </article>

  <h2 class="promo-title">LOREM IPSUM DOLOR SIT AMET SED UT IPSORODIUM</h2>
  <p class="promo-sub">Temporibus autem quibusdam et aut officiis debitis aut rerum</p>
  <div class="more">MORE
    <svg width="32" height="32" viewBox="0 0 32 32"><circle cx="16" cy="16" r="14.5" fill="none" stroke="#1f2a30" stroke-width="2"/><path d="M13 9l7 7-7 7" fill="none" stroke="#1f2a30" stroke-width="2.6"/></svg>
  </div>
</div>
</body>
</html>
```